Verpackungen für Schwangerschaftsfotograf
sehr tolle und schnelle Umsetzungen meiner Wünsche - vielen Dank für die gute Zusammenarbeit
Zielgruppe
Fotograf mit Spezialisierung auf Schwangerschaft und Neugeborene
Aufgabenstellung
ich brauche ein Layout für diese Verpackung
https://www.faltwerk-muster.de/download/klappbox/Druckvorlage_FaltwerkMuster_Klappbox-30.pdf
ich stelle mir das vom Design her so vor wie eine Holzkiste:
https://www.bildervorrat-beispiel.com/de/image-photo/wooden-box-483910275?src=QkTzvLwe8pRnYd42h71xkc-1-27
Und wie der Text irgendwie mein Logo integrieren.
Die Schachtel soll eine neue Verpackung werden um Abzüge und USB Stick zu übergeben

```html
<!DOCTYPE html>
<html lang="de">
<head>
<meta charset="utf-8">
<title>Klappbox Holzkiste – Druckvorlage</title>
<link rel="stylesheet" href="https://fonts.googleapis.com/css2?family=Alegreya:ital,wght@0,700;1,700&family=Alegreya+SC:wght@700&display=swap">
<style>
  :root {
    --paper: #ffffff;
    --wood-light: #a8703c;
    --wood-mid: #8a5530;
    --wood-dark: #5e3a20;
    --plank: #6f4426;
    --plank-edge: #4a2c17;
    --strap: #b27a2c;
    --strap-dark: #6a4216;
    --nail: #3a2414;
    --ink: #1a0f08;
    --dieline: #e0157a;
  }
  html, body {
    margin: 0;
    width: 1200px;
    height: 951px;
    overflow: hidden;
    background: var(--paper);
  }
  .dieline-sheet { display: block; width: 1200px; height: 951px; }
  .panel { stroke: none; }
  .plank { fill: var(--plank); stroke: var(--plank-edge); stroke-width: .6; }
  .strap { fill: url(#strapTone); stroke: var(--strap-dark); stroke-width: .6; }
  .nail { fill: var(--nail); }
  .fold, .cut { fill: none; stroke: var(--dieline); stroke-width: .6; }
  .brand-name { font-family: "Alegreya SC", serif; font-weight: 700; font-size: 7.6px; fill: var(--ink); letter-spacing: .2px; }
  .brand-url { font-family: "Alegreya", serif; font-style: italic; font-weight: 700; font-size: 6.4px; fill: var(--ink); }
  .brand-dot { fill: none; stroke: var(--ink); stroke-width: .9; }
</style>
</head>
<body>
<svg class="dieline-sheet" viewBox="0 0 1200 951" xmlns="http://www.w3.org/2000/svg">
  <defs>
    <linearGradient id="woodTone" x1="0" y1="0" x2="1" y2="1">
      <stop offset="0" stop-color="#9a6232"/>
      <stop offset=".45" stop-color="#a8754a"/>
      <stop offset=".7" stop-color="#8a5a34"/>
      <stop offset="1" stop-color="#a06a36"/>
    </linearGradient>
    <linearGradient id="woodBand" x1="0" y1="0" x2="0" y2="1">
      <stop offset="0" stop-color="#7a4a26"/>
      <stop offset=".5" stop-color="#9a6232"/>
      <stop offset="1" stop-color="#6e4222"/>
    </linearGradient>
    <linearGradient id="strapTone" x1="0" y1="0" x2="1" y2="0">
      <stop offset="0" stop-color="#7a4c1a"/>
      <stop offset=".5" stop-color="#c08a3a"/>
      <stop offset="1" stop-color="#7a4c1a"/>
    </linearGradient>
  </defs>

  <!-- Deckel-Lasche -->
  <g class="lid-flap">
    <rect class="panel" x="324" y="363" width="356" height="47" fill="url(#woodBand)" role="img" aria-label="Holzmaserung, alte Bretter"/>
    <line class="fold" x1="354" y1="363" x2="354" y2="410"/>
    <line class="fold" x1="650" y1="363" x2="650" y2="410"/>
    <path class="cut" d="M354 368 H331 Q327 368 327 372 V404 Q327 408 331 408 H354"/>
    <path class="cut" d="M650 368 H673 Q677 368 677 372 V404 Q677 408 673 408 H650"/>
    <path class="cut" d="M483 363 Q495 376 507 363"/>
    <circle class="nail" cx="373" cy="375" r="1.3"/><circle class="nail" cx="373" cy="398" r="1.3"/>
    <circle class="nail" cx="634" cy="375" r="1.3"/><circle class="nail" cx="634" cy="398" r="1.3"/>
    <g class="brand-lockup" transform="rotate(180 495 392)">
      <circle class="brand-dot" cx="448" cy="390" r="5"/>
      <text class="brand-name" x="460" y="390">LENNART BERGHOFF</text>
      <text class="brand-url" x="460" y="398">babyfotos-musterstadt.de</text>
    </g>
  </g>

  <!-- Deckel -->
  <g class="lid">
    <rect class="panel" x="307" y="410" width="388" height="185" fill="url(#woodTone)" role="img" aria-label="Holzmaserung, verwitterte Kistenbretter"/>
    <rect class="plank" x="359" y="410" width="41" height="185"/>
    <rect class="plank" x="604" y="410" width="41" height="185"/>
    <rect class="strap" x="369" y="438" width="21" height="127"/>
    <rect class="strap" x="613" y="438" width="21" height="127"/>
    <circle class="nail" cx="379" cy="448" r="1.2"/><circle class="nail" cx="379" cy="502" r="1.2"/><circle class="nail" cx="379" cy="555" r="1.2"/>
    <circle class="nail" cx="623" cy="448" r="1.2"/><circle class="nail" cx="623" cy="502" r="1.2"/><circle class="nail" cx="623" cy="555" r="1.2"/>
    <line class="fold" x1="359" y1="410" x2="359" y2="595"/>
    <line class="fold" x1="645" y1="410" x2="645" y2="595"/>
    <line class="fold" x1="324" y1="410" x2="680" y2="410"/>
    <path class="cut" d="M359 414 L315 416 Q311 420 312 430 L313 582 Q314 590 322 591 L359 593"/>
    <path class="cut" d="M645 414 L689 416 Q693 420 692 430 L691 582 Q690 590 682 591 L645 593"/>
    <g class="brand-lockup" transform="rotate(180 495 455)">
      <circle class="brand-dot" cx="448" cy="453" r="5"/>
      <text class="brand-name" x="460" y="453">LENNART BERGHOFF</text>
      <text class="brand-url" x="460" y="461">babyfotos-musterstadt.de</text>
    </g>
  </g>

  <!-- Rückwand / Scharnier -->
  <g class="hinge-band">
    <rect class="panel" x="260" y="595" width="484" height="48" fill="url(#woodBand)" role="img" aria-label="Holzmaserung, Querbrett"/>
    <line class="fold" x1="260" y1="595" x2="744" y2="595"/>
    <line class="fold" x1="354" y1="595" x2="354" y2="643"/>
    <line class="fold" x1="650" y1="595" x2="650" y2="643"/>
    <line class="fold" x1="354" y1="643" x2="650" y2="643"/>
    <path class="cut" d="M354 599 H268 Q264 599 264 603 V634 Q264 638 268 638 H354"/>
    <path class="cut" d="M650 599 H736 Q740 599 740 603 V634 Q740 638 736 638 H650"/>
    <circle class="nail" cx="373" cy="608" r="1.3"/><circle class="nail" cx="373" cy="631" r="1.3"/>
    <circle class="nail" cx="633" cy="608" r="1.3"/><circle class="nail" cx="633" cy="631" r="1.3"/>
    <g class="brand-lockup">
      <circle class="brand-dot" cx="448" cy="617" r="5"/>
      <text class="brand-name" x="460" y="618">LENNART BERGHOFF</text>
      <text class="brand-url" x="460" y="626">babyfotos-musterstadt.de</text>
    </g>
  </g>

  <!-- Boden -->
  <g class="base">
    <rect class="panel" x="240" y="643" width="523" height="186" fill="url(#woodTone)" role="img" aria-label="Holzmaserung, Kistenboden mit Seitenwänden"/>
    <rect class="plank" x="352" y="643" width="40" height="186"/>
    <rect class="plank" x="611" y="643" width="40" height="186"/>
    <rect class="plank" x="392" y="656" width="219" height="42"/>
    <circle class="nail" cx="384" cy="652" r="1.2"/><circle class="nail" cx="384" cy="820" r="1.2"/>
    <circle class="nail" cx="618" cy="652" r="1.2"/><circle class="nail" cx="618" cy="820" r="1.2"/>
    <line class="fold" x1="352" y1="643" x2="352" y2="829"/>
    <line class="fold" x1="651" y1="643" x2="651" y2="829"/>
    <line class="fold" x1="303" y1="643" x2="303" y2="829"/>
    <line class="fold" x1="700" y1="643" x2="700" y2="829"/>
    <path class="cut" d="M303 648 H258 Q254 648 254 654 V690 L259 694 V778 L254 782 V818 Q254 824 258 824 H303"/>
    <path class="cut" d="M700 648 H745 Q749 648 749 654 V690 L744 694 V778 L749 782 V818 Q749 824 745 824 H700"/>
  </g>

  <!-- Vorderwand -->
  <g class="front-flap">
    <rect class="panel" x="261" y="829" width="482" height="46" fill="url(#woodBand)" role="img" aria-label="Holzmaserung, Frontbrett"/>
    <line class="fold" x1="261" y1="829" x2="743" y2="829"/>
    <line class="fold" x1="356" y1="829" x2="356" y2="875"/>
    <line class="fold" x1="648" y1="829" x2="648" y2="875"/>
    <path class="cut" d="M356 833 H268 Q265 833 265 837 V868 Q265 872 268 872 H356"/>
    <path class="cut" d="M648 833 H736 Q739 833 739 837 V868 Q739 872 736 872 H648"/>
    <circle class="nail" cx="373" cy="841" r="1.3"/><circle class="nail" cx="373" cy="864" r="1.3"/>
    <circle class="nail" cx="633" cy="841" r="1.3"/><circle class="nail" cx="633" cy="864" r="1.3"/>
    <g class="brand-lockup" transform="rotate(180 495 850)">
      <circle class="brand-dot" cx="448" cy="848" r="5"/>
      <text class="brand-name" x="460" y="848">LENNART BERGHOFF</text>
      <text class="brand-url" x="460" y="856">babyfotos-musterstadt.de</text>
    </g>
  </g>
</svg>
</body>
</html>
```